Weight Management Brochure

I would like to take the information on our website tarnwellnessplan.org and translate this into a professional brochure.
There is information about our weight management program that is similar to the marketing of the company quivofit.com which can be used as a resource as well. details of our service as outlined on our website tarnwellnessplan.org, facebook and instagram logo, website, address, phone number, logo. health related images

Target Market(s)

18 and older, men and women interested in weight management services

Industry/Entity Type

Nutrition

Requirements
Must have
• SERVICES
• Medically supervised weight management through collaboration with Physician or Nurse Practitioner, and Registered Dietician
• Weight Loss Prescription management
• Body composition scale analysis at every office visit
• Customized determination of ideal weight and personalized caloric/nutrient needs
• Analysis of daily eating patterns, nutritional education, and personalized nutrition planning support
• Medical nutrition therapy for variety of disease states including: diabetes, cardiovascular disease, hypertension, high cholesterol, gastrointestinal disorders, and sleep apnea
• Nutrition counseling for all weight goals (weight loss, maintenance, or gain)
• Individualized menu planning, healthy eating habit education and advice, custom exercise prescription
• Cognitive behavior therapy, motivational interviewing
• Full and Partial meal replacement optionsOPTIONS
• Visit Options
• Medical Consultation and follow ups
• Registered Dietitian Consultation and follow ups
• Daily Health coaching
• Online Virtual Medical, Dietitian or Health Coaching Virtual visits
Nice to have
• Bio's of the providers if room is available
Should not have
• pictures of people (man or woman) unless its non discriminatory

```html
<!DOCTYPE html>
<html lang="en">
<head>
<meta charset="utf-8">
<title>Tarn Wellness – Weight Management Brochure</title>
<link href="https://fonts.googleapis.com/css2?family=Anton&family=Roboto:wght@700&family=Source+Sans+3:wght@400;600;700&display=swap" rel="stylesheet">
<style>
:root{
  --stage:#4a4e57;
  --blue:#2a72b5;
  --blue-dark:#1d5c9c;
  --blue-light:#3a88cc;
  --navy:#283142;
  --teal:#1bb3c8;
  --cyan:#1fd2e8;
  --white:#ffffff;
  --ink:#1f2633;
  --grey:#d4d7dc;
}
*{margin:0;padding:0;box-sizing:border-box}
html,body{width:1200px;height:1200px;overflow:hidden;background:var(--stage)}
body{position:relative;font-family:"Source Sans 3",sans-serif;color:var(--white)}
.spread{position:absolute;left:254px;width:698px;height:541px;overflow:hidden;box-shadow:0 4px 12px rgba(0,0,0,.35)}
.spread--outside{top:36px}
.spread--inside{top:612px}
.spread-bg{position:absolute;left:0;top:0;width:698px;height:541px}

/* providers */
.provider-photo{position:absolute;width:54px;height:54px;border-radius:50%;border:3px solid var(--white);background:radial-gradient(circle at 50% 40%,#c9b3a3,#6b4b3e 75%)}
.name-pill{position:absolute;height:14px;border-radius:8px;background:var(--teal);font:700 9.6px/14px "Roboto",sans-serif;text-align:center;color:var(--white)}
.bio{position:absolute;left:10px;width:210px;font-size:7.7px;line-height:10.4px;text-align:center}

/* brand */
.brand{position:absolute;display:flex;align-items:center;gap:5px;font-weight:700;white-space:nowrap}
.brand-dot{border-radius:50%;flex:none}

/* contact */
.contact{position:absolute;left:240px;width:212px;text-align:center;color:var(--ink)}
.contact-lead{font-size:11px;line-height:14px}
.phone-icon{display:block;margin:0 auto}
.phone-number{font-size:10.5px;line-height:13px}
.hours{position:absolute;left:270px;width:160px;color:var(--ink);font-size:10.5px;line-height:15px;font-weight:600}
.hours-title{border-bottom:1px solid var(--ink);padding-bottom:2px;margin-bottom:4px}
.hours em{font-style:normal;color:var(--teal)}
.url-pill{position:absolute;height:18px;border-radius:9px;background:var(--teal);font-size:9.5px;line-height:18px;font-weight:700;text-align:center;color:var(--white)}

/* title */
.title{position:absolute;left:470px;width:216px;text-align:center;font-family:"Anton",sans-serif;line-height:1}
.title-main{font-size:57px;color:var(--cyan);letter-spacing:1px}
.title-sub{font-size:30px;color:var(--white);margin-top:3px}

.photo{position:absolute}

/* inside */
.heading-pill{position:absolute;height:25px;border-radius:13px;background:var(--navy);font:20px/25px "Anton",sans-serif;text-align:center;color:var(--white);letter-spacing:.3px}
.heading-pill--services{background:var(--teal);border:2px solid var(--navy);line-height:21px;color:var(--navy)}
.body-copy{position:absolute;left:14px;font-size:10px;line-height:12.6px;white-space:nowrap}
.services{position:absolute;left:246px;width:200px;top:66px;height:450px;display:flex;flex-direction:column;justify-content:space-between;color:var(--ink);font-size:8px;line-height:10.4px;text-align:center;list-style:none;white-space:nowrap}
.services li::before{content:"";display:block;width:6px;height:6px;border:1px solid var(--ink);transform:rotate(45deg);margin:0 auto 6px}
.option-label{position:absolute;height:17px;padding:0 7px;border-radius:9px;background:var(--teal);border:1.5px solid var(--white);font-size:11px;line-height:14px;color:var(--white)}
.option-rule{position:absolute;height:1px;background:var(--white);right:16px}
.option-text{position:absolute;font-size:8px;line-height:10.4px;white-space:nowrap}
.option-text strong{font-weight:700}
</style>
</head>
<body>

<section class="spread spread--outside">
  <svg class="spread-bg" viewBox="0 0 698 541" aria-hidden="true">
    <defs>
      <linearGradient id="blueOut" x1="0" x2="1" y1="0" y2="1">
        <stop offset="0" stop-color="#1d5c9c"/><stop offset="1" stop-color="#3a88cc"/>
      </linearGradient>
      <linearGradient id="whiteOut" x1="0" x2="1">
        <stop offset="0" stop-color="#e6e8eb"/><stop offset=".5" stop-color="#ffffff"/><stop offset="1" stop-color="#e6e8eb"/>
      </linearGradient>
    </defs>
    <rect width="698" height="541" fill="url(#blueOut)"/>
    <path d="M222,0 H474 C484,80 440,170 445,250 C450,330 484,420 474,541 H226 C214,420 248,330 250,250 C252,170 212,80 222,0Z" fill="#283142"/>
    <path d="M236,0 H462 C470,80 428,170 432,250 C436,330 470,420 460,541 H240 C228,420 262,330 264,250 C266,170 226,80 236,0Z" fill="url(#whiteOut)"/>
    <path d="M262,40 C250,120 282,190 280,250 C278,320 246,400 256,500" stroke="#c9ccd2" stroke-width="3" fill="none"/>
    <path d="M436,40 C448,120 416,190 418,250 C420,320 452,400 442,500" stroke="#c9ccd2" stroke-width="3" fill="none"/>
    <path d="M232,244 C240,332 456,332 462,244" stroke="#1bb3c8" stroke-width="5" fill="none"/>
  </svg>

  <div class="provider-photo" style="left:86px;top:21px" role="img" aria-label="Portrait photo of Dr. Lowell Sterling"></div>
  <div class="name-pill" style="left:53px;top:88px;width:124px">Dr. Lowell Sterling</div>
  <p class="bio" style="top:109px">Dr. Lowell Sterling has been practicing Internal Medicine and Geriatrics for over 30 years. He has always concentrated his efforts on giving very personalized care to all his patients by concentrating on preventative medicine and maintaining good health.</p>

  <div class="provider-photo" style="left:86px;top:183px" role="img" aria-label="Portrait photo of Dr. Julian Moreno"></div>
  <div class="name-pill" style="left:49px;top:253px;width:128px">Dr. Julian Moreno</div>
  <p class="bio" style="top:274px">Julian Moreno, MD, FACP, FACE, is an Associate Professor of Medicine at the Halden School of Medicine at Halden University and is Vice President at Brookfield Internal Medicine Group in Eastmere, New York. He earned his medical degree at the Larkmoor University School of Medicine in Larkmoor.</p>

  <div class="provider-photo" style="left:78px;top:369px" role="img" aria-label="Portrait photo of Dr. Colin Grayson"></div>
  <div class="name-pill" style="left:37px;top:435px;width:126px">Dr. Colin Grayson</div>
  <p class="bio" style="top:460px">Dr. Colin Grayson is a native New Yorker born and raised in Bayshore. He completed his undergraduate studies at Eastmoor State University followed by a drastic climate change when he attended medical school at the Redvale University Southwest Campus.</p>

  <div class="brand" style="left:296px;top:68px;font-size:12px;color:var(--navy)"><span class="brand-dot" style="width:12px;height:12px;background:var(--navy)"></span>Tarn Wellness</div>

  <div class="contact" style="top:128px">
    <p class="contact-lead">Our staff will gladly schedule<br>you for an appointment:</p>
  </div>
  <div class="contact" style="top:182px">
    <svg class="phone-icon" width="14" height="11" viewBox="0 0 14 11" aria-hidden="true"><path d="M1,4 C1,1 13,1 13,4 L11,5 9,3 5,3 3,5Z M3,6 H11 L12,11 H2Z" fill="#283142"/><circle cx="7" cy="8" r="1.6" fill="#fff"/></svg>
    <p class="phone-number">555.214.8100</p>
  </div>
  <div class="contact" style="top:234px">
    <svg class="phone-icon" width="12" height="12" viewBox="0 0 12 12" aria-hidden="true"><path d="M2,1 L4,1 5,4 3.5,5 C4.5,7 5,7.5 7,8.5 L8,7 11,8 11,10 C11,11 10,11.5 9,11.5 C4,11 1,8 0.5,3 C0.5,2 1,1 2,1Z" fill="#283142"/></svg>
    <p class="phone-number">555.214.7348</p>
  </div>

  <div class="hours" style="top:348px">
    <p class="hours-title">Administrative Office Hours:</p>
    <p>Monday <em>10am-8pm</em></p>
    <p>Tuesday-<em>Friday 9am-5pm</em></p>
  </div>

  <div class="photo" style="left:290px;top:408px;width:116px;height:100px;border-radius:48% 48% 44% 44%;background:radial-gradient(circle at 40% 40%,#e0433d,#a3161a 75%)" role="img" aria-label="Red apple with a weighing scale dial and a green leaf"></div>
  <div class="url-pill" style="left:263px;top:511px;width:167px">www.tarnwellnessplan.org</div>

  <div class="brand" style="left:528px;top:66px;font-size:18px;color:var(--white)"><span class="brand-dot" style="width:16px;height:16px;background:var(--white)"></span>Tarn Wellness</div>

  <div class="title" style="top:166px">
    <p class="title-main">WEIGHT</p>
    <p class="title-sub">MANAGEMENT</p>
    <p class="title-sub">SERVICES</p>
  </div>

  <div class="photo" style="left:474px;top:330px;width:216px;height:160px;border-radius:14px;transform:rotate(12deg);background:linear-gradient(135deg,#2a2f38,#0f1116 60%,#c9dfee)" role="img" aria-label="Bathroom scale with a red apple and a tape measure"></div>
  <div class="url-pill" style="left:493px;top:511px;width:165px">www.tarnwellnessplan.org</div>
</section>

<section class="spread spread--inside">
  <svg class="spread-bg" viewBox="0 0 698 541" aria-hidden="true">
    <defs>
      <linearGradient id="blueIn" x1="0" x2="1" y1="0" y2="1">
        <stop offset="0" stop-color="#1d5c9c"/><stop offset="1" stop-color="#3a88cc"/>
      </linearGradient>
      <linearGradient id="whiteIn" x1="0" x2="1">
        <stop offset="0" stop-color="#e6e8eb"/><stop offset=".5" stop-color="#ffffff"/><stop offset="1" stop-color="#e6e8eb"/>
      </linearGradient>
    </defs>
    <rect width="698" height="541" fill="url(#blueIn)"/>
    <path d="M212,0 H488 C462,80 448,150 462,240 C476,330 462,440 482,541 H176 C190,430 252,330 248,240 C244,150 204,80 212,0Z" fill="#283142"/>
    <path d="M224,0 H476 C450,80 436,150 450,240 C464,330 450,440 470,541 H188 C202,430 264,330 260,240 C256,150 216,80 224,0Z" fill="url(#whiteIn)"/>
    <path d="M240,30 C236,110 276,170 272,240 C268,320 226,420 218,520" stroke="#c9ccd2" stroke-width="3" fill="none"/>
    <path d="M458,30 C436,110 424,170 436,240 C448,320 438,420 454,520" stroke="#c9ccd2" stroke-width="3" fill="none"/>
  </svg>

  <div class="heading-pill" style="left:49px;top:10px;width:112px">About Us</div>
  <p class="body-copy" style="top:42px">Online or onsite Personalized and<br>medically supervised and technology<br>integrated weight management program</p>

  <div class="heading-pill" style="left:56px;top:95px;width:94px">Misson</div>
  <p class="body-copy" style="top:128px">Tarn Wellness was founded<br>based on the understanding that no two<br>people are the same. We offer a unique<br>approach and partner with our patients to<br>create individualized plans based on both<br>short-term and long-term-goals. Whether your<br>goal is to lose 15 pounds or 150 pounds, lower<br>your blood sugar, blood pressure or the amount of<br>“pills” you take in a day, or simply just to feel better<br>about yourself when you look in the mirror, we<br>can help. Our providers offer personalized,<br>medically supervised plans and support patients<br>to achieve and maintain weight loss, as well as<br>to help them improve their overall health<br>status.</p>
  <p class="body-copy" style="top:324px">Each plan is tailored specifically for each<br>patient by utilizing state of the art,<br>non-invasive, diagnostic testing which<br>helps us to determine an individual's<br>own metabolic needs and therefore<br>guides us in establishing a plan that<br>is created just for them.</p>

  <div class="photo" style="left:0;top:424px;width:106px;height:117px;border-radius:0 50% 0 0;background:radial-gradient(circle at 40% 50%,#c8303a,#3b3566 70%,#d9c7b0)" role="img" aria-label="Heart-shaped bowl filled with berries, cherries and tomatoes"></div>

  <div class="heading-pill heading-pill--services" style="left:286px;top:10px;width:112px">SERVICES</div>
  <ul class="services">
    <li>Medically supervised weight management through<br>collaboration with Physician or Nurse Practitioner, and<br>Registered Dietician</li>
    <li>Weight Loss Prescription management</li>
    <li>Body composition scale analysis at every<br>office visit</li>
    <li>Customized determination<br>of ideal weight and personalized<br>caloric/nutrient needs</li>
    <li>Analysis of daily eating<br>patterns, nutritional education,<br>and personalized nutrition<br>planning support</li>
    <li>Medical nutrition therapy for<br>variety of disease states including: diabetes,<br>cardiovascular disease, hypertension,<br>high cholesterol, gastrointestinal disorders, and sleep<br>apnea</li>
    <li>Nutrition counseling for all weight goals (weight loss,<br>maintenance, or gain)</li>
    <li>Individualized menu planning, healthy eating habit<br>education and advice, custom exercise prescription</li>
    <li>Cognitive behavior therapy, motivational interviewing</li>
    <li>Full and Partial meal replacement optionsOPTIONS</li>
  </ul>

  <div class="heading-pill" style="left:539px;top:10px;width:113px">OPTIONS</div>

  <div class="option-rule" style="left:515px;top:46px"></div>
  <div class="option-label" style="left:461px;top:38px">Option 1</div>
  <p class="option-text" style="left:506px;top:64px">Medical visits with <strong>Dr. Grayson</strong><br>Initial <strong>$350</strong><br>Follow up <strong>$150</strong><br>Registered Dietitian follow up <strong>$75</strong><br>Daily Health coaching with dietician <strong>$50/week</strong></p>

  <div class="option-rule" style="left:490px;top:150px"></div>
  <div class="option-label" style="left:436px;top:142px">Option 2</div>
  <p class="option-text" style="left:480px;top:166px">Medical visits with <strong>Nurse Practitioner Jenna Oakley</strong><br>Initial <strong>$250</strong><br>Follow up <strong>$100</strong><br>Registered Dietician follow up <strong>$75</strong><br>Daily Health Coaching with dietitian <strong>$50/week</strong></p>

  <div class="option-rule" style="left:492px;top:257px"></div>
  <div class="option-label" style="left:437px;top:249px">Option 3</div>
  <p class="option-text" style="left:505px;top:270px"><strong>Registered Dietician visits</strong><br>Initial <strong>$100</strong><br>Follow up <strong>$75</strong><br>Daily Health coaching <strong>$50/week</strong><br>Dr. Grayson visits <strong>25% off</strong><br>Jenna Oakley visits <strong>25% off</strong></p>

  <div class="option-rule" style="left:530px;top:370px"></div>
  <div class="option-label" style="left:470px;top:362px">Option 4</div>
  <p class="option-text" style="left:534px;top:382px">Online Visits<br><strong>Initial dietitian visit (or included in….)</strong><br>Health Coaching option <strong>$75</strong><br>Follow up Registered Dietician <strong>$50</strong></p>

  <div class="photo" style="left:470px;top:440px;width:228px;height:101px;border-radius:60% 40% 0 0;background:radial-gradient(circle at 55% 45%,#9bd24a,#4f9a25 40%,#d8dde2 70%,transparent 72%)" role="img" aria-label="Green apple wrapped in a tape measure"></div>
</section>

</body>
</html>
```